Business Card Design

We need a design that will also transfer to car decals
We need a design that will speak to the average person needing home and office remodeling
The design should be fresh, exciting, easy to read in a glance and unique
We would like a die-cut tool belt
Bright colors and evenly spaced information

Target Market(s)

Home and business owners
Middle and Upper Income property owners
Families and people with fixer upper homes

Industry/Entity Type

Business

Contact Information for Business Card

Looking for the best Bay Area Handyman? Here I am!
RKW Handyman Services does it all at prices regular people can afford.
Electrical, Plumbing, Carpentry, Remodeling, Fencing, Picture and window placement, Hauling ... and anything else you can imagine!
510-374-2196
Serving the Entire Bay Area
Free Estimates! Call us Today to turn your dreams into reality!

Font styles to use
Serif

Requirements
Must have
• Speaks to the average person
stands out among similar industry cards
Nice to have
• fun, comical, you want to hold on to this card
Should not have
• bland colors
look too crowded

```html
<!DOCTYPE html>
<html lang="en">
<head>
<meta charset="utf-8">
<title>RKW Handyman Services – Business Card</title>
<link href="https://fonts.googleapis.com/css2?family=Cinzel:wght@400;700&family=Marcellus&family=Spectral:wght@300;400&display=swap" rel="stylesheet">
<style>
  :root {
    --page-bg: #e3e3e1;
    --card-bg: #ffffff;
    --green: #6a9e3f;
    --green-dark: #4f7b33;
    --ink: #4a4a4a;
    --ink-soft: #5e5e5e;
    --white: #ffffff;
  }
  * { margin: 0; padding: 0; box-sizing: border-box; }
  html, body {
    width: 1200px; height: 1200px; overflow: hidden;
    background: var(--page-bg);
  }
  .sheet { position: relative; width: 1200px; height: 1200px; }

  .card {
    position: absolute; left: 150px; width: 900px; height: 514px;
    background: var(--card-bg);
    box-shadow: 0 2px 10px rgba(0,0,0,0.12);
    overflow: hidden;
  }
  .card--front { top: 50px; }
  .card--back { top: 636px; }

  .brand-name {
    font-family: "Cinzel", serif; font-weight: 700;
    color: var(--green); line-height: 1;
  }
  .brand-tagline {
    font-family: "Marcellus", serif; color: var(--ink);
    letter-spacing: 0.22em; text-transform: uppercase;
  }

  /* Front */
  .front-logo {
    position: absolute; top: 150px; left: 0; right: 0;
    text-align: center;
  }
  .front-logo .brand-name { font-size: 76px; }
  .front-logo .brand-tagline { font-size: 21px; margin-top: 16px; }

  /* Bands */
  .band {
    position: absolute; left: 0; right: 0;
    background: var(--green);
    border-bottom: 20px solid var(--green-dark);
  }
  .band--footer { bottom: 0; height: 86px; }
  .band-mark {
    position: absolute; right: 28px; bottom: 6px;
    font-family: "Cinzel", serif; font-weight: 400;
    color: var(--white); font-size: 40px; line-height: 1;
  }

  /* Back */
  .back-logo {
    position: absolute; top: 30px; left: 40px;
    display: flex; align-items: flex-end; gap: 18px;
  }
  .back-logo .brand-name { font-size: 62px; }
  .back-logo .brand-tagline { font-size: 17px; padding-bottom: 6px; }

  .intro-row {
    position: absolute; top: 118px; left: 40px; right: 40px;
    display: flex; align-items: flex-start;
    font-family: "Spectral", serif; font-weight: 300;
    color: var(--ink-soft); font-size: 17px; line-height: 1.62;
    letter-spacing: 0.06em;
  }
  .intro-pitch { width: 395px; }
  .intro-divider {
    width: 1px; height: 96px; background: var(--ink);
    margin: 8px 26px 0 22px; flex: none;
  }
  .intro-services { flex: 1; }

  .band--call {
    top: 246px; height: 80px;
    display: flex; align-items: center; padding-left: 40px;
  }
  .call-text {
    font-family: "Marcellus", serif; color: var(--white);
    font-size: 31px; letter-spacing: 0.16em; white-space: nowrap;
    margin-top: -6px;
  }
  .call-number { margin-left: 44px; }

  .closing {
    position: absolute; top: 342px; left: 40px; right: 40px;
    font-family: "Spectral", serif; font-weight: 400;
    color: var(--ink); font-size: 27px; line-height: 1.35;
  }
</style>
</head>
<body>
<main class="sheet">

  <section class="card card--front" aria-label="Card front">
    <div class="front-logo">
      <div class="brand-name">RKW</div>
      <div class="brand-tagline">Handyman | Services</div>
    </div>
    <div class="band band--footer">
      <span class="band-mark">RKW</span>
    </div>
  </section>

  <section class="card card--back" aria-label="Card back">
    <div class="back-logo">
      <div class="brand-name">RKW</div>
      <div class="brand-tagline">Handyman | Services</div>
    </div>

    <div class="intro-row">
      <p class="intro-pitch">Looking for the best Bay Area Handyman? Here I am! RKW Handyman Services does it all at prices regular people can afford</p>
      <span class="intro-divider" aria-hidden="true"></span>
      <p class="intro-services">Electrical. Plumbing. Carpentry Remodeling. Fencing. Picture and window placement. Hauling and anything else you can imagine!</p>
    </div>

    <div class="band band--call">
      <p class="call-text">CALL US NOW:<span class="call-number">510-374-2196</span></p>
    </div>

    <div class="closing">
      <p>Serving the Entire Bay Area Free Estimates!</p>
      <p>Call us Today to turn your dreams into reality!</p>
    </div>

    <div class="band band--footer">
      <span class="band-mark">RKW</span>
    </div>
  </section>

</main>
</body>
</html>
```